New start-up company catalog!

Heat transfer printing company. We are set to launch later this month and need a stand out catalog to wow our customers. We are a printing/manufacturing heat transfer company geared towards apparel and promotional items.

```html
<!DOCTYPE html>
<html lang="en">
<head>
<meta charset="utf-8">
<title>Northline Prints – Catalog Covers</title>
<link rel="stylesheet" href="https://fonts.googleapis.com/css2?family=Anton&family=Montserrat:wght@700;800&display=swap">
<style>
  :root {
    --page-bg: #e4e4e6;
    --paper-light: #f4f4f5;
    --paper-mid: #d9d9dc;
    --brand-purple: #2d2a74;
    --brand-purple-soft: #5c54a8;
    --brand-teal: #6fd3d3;
    --brand-orange: #e9a51e;
    --ink-dark: #1d1b3a;
  }
  * { box-sizing: border-box; margin: 0; padding: 0; }
  html, body {
    width: 1200px;
    height: 900px;
    overflow: hidden;
    background: var(--page-bg);
    font-family: "Montserrat", Arial, sans-serif;
  }
  .canvas { position: relative; width: 1200px; height: 900px; }

  .cover {
    position: absolute;
    width: 540px;
    height: 370px;
    overflow: hidden;
    background: linear-gradient(135deg, var(--paper-light) 0%, var(--paper-mid) 100%);
    box-shadow: 0 10px 24px rgba(0, 0, 0, 0.18);
  }
  .cover--front { left: 120px; top: 100px; }
  .cover--back { left: 540px; top: 480px; }
  .cover__shapes { position: absolute; inset: 0; }

  .brand {
    position: absolute;
    display: flex;
    align-items: center;
    gap: 10px;
  }
  .brand__square {
    width: 26px;
    height: 26px;
    background: var(--brand-purple);
  }
  .brand__name {
    font-family: "Montserrat", Arial, sans-serif;
    font-weight: 800;
    font-size: 28px;
    color: var(--brand-purple);
    letter-spacing: -0.5px;
  }
  .cover--front .brand { left: 108px; top: 48px; }
  .cover--back .brand { left: 50px; top: 72px; }

  .headline {
    position: absolute;
    font-family: "Anton", Impact, sans-serif;
    text-transform: uppercase;
    letter-spacing: 1px;
    line-height: 1;
    transform: skewX(-8deg);
  }
  .headline--quality { left: 262px; top: 98px; font-size: 38px; color: var(--brand-orange); }
  .headline--transfers { left: 148px; top: 140px; font-size: 38px; color: var(--brand-teal); }

  .product-showcase {
    position: absolute;
    left: 104px;
    top: 196px;
    width: 312px;
    height: 162px;
    background: linear-gradient(90deg, #f1f1f1 0%, #cfcfd2 30%, #2a2a2e 50%, #3a3a40 65%, #d6d6da 78%, #2f6fa4 90%, #3f9fd6 100%);
    opacity: 0.9;
  }

  .contact-web {
    position: absolute;
    left: 130px;
    top: 210px;
    width: 230px;
    height: 24px;
    background: var(--brand-orange);
    clip-path: polygon(4% 0, 100% 0, 100% 100%, 0 100%);
    display: flex;
    align-items: center;
    justify-content: center;
    font-weight: 800;
    font-size: 13px;
    color: var(--ink-dark);
  }
  .contact-phone {
    position: absolute;
    left: 0;
    top: 244px;
    width: 320px;
    height: 62px;
    background: var(--brand-purple);
    display: flex;
    align-items: center;
    padding-left: 40px;
    font-weight: 800;
    font-size: 30px;
    color: var(--brand-orange);
    letter-spacing: 0.5px;
  }
</style>
</head>
<body>
<main class="canvas">

  <section class="cover cover--front" aria-label="Catalog front cover">
    <svg class="cover__shapes" viewBox="0 0 540 370" width="540" height="370" aria-hidden="true">
      <polygon class="band-left" points="0,0 62,0 80,370 0,370" fill="var(--brand-purple)"/>
      <polygon class="band-right" points="416,0 540,0 540,370 430,370" fill="var(--brand-teal)"/>
      <rect class="accent-line-orange" x="94" y="52" width="6" height="150" fill="var(--brand-orange)"/>
      <rect class="accent-line-purple" x="418" y="180" width="5" height="190" fill="var(--brand-purple)"/>
    </svg>
    <div class="brand">
      <span class="brand__square"></span>
      <span class="brand__name">Northline Prints</span>
    </div>
    <p class="headline headline--quality">Quality</p>
    <p class="headline headline--transfers">Heat Transfers</p>
    <div class="product-showcase" role="img" aria-label="Printed white and black t-shirts and a blue drawstring bag"></div>
  </section>

  <section class="cover cover--back" aria-label="Catalog back cover">
    <svg class="cover__shapes" viewBox="0 0 540 370" width="540" height="370" aria-hidden="true">
      <defs>
        <linearGradient id="panelShade" x1="0" y1="0" x2="1" y2="0">
          <stop offset="0" stop-color="var(--brand-purple)"/>
          <stop offset="1" stop-color="var(--brand-purple-soft)"/>
        </linearGradient>
      </defs>
      <polygon class="panel-right" points="340,0 540,0 540,370 348,370" fill="url(#panelShade)"/>
      <rect class="accent-line-teal" x="330" y="130" width="5" height="240" fill="var(--brand-teal)"/>
    </svg>
    <div class="brand">
      <span class="brand__square"></span>
      <span class="brand__name">Northline Prints</span>
    </div>
    <p class="contact-web">www.northlineprints.com</p>
    <p class="contact-phone">0198 765 432</p>
  </section>

</main>
</body>
</html>
```